Bluestone Auto Works | ||
Bluestone | ||
Automotive | ||
Bluestone Auto Works is a auto reseller, that offers consignment, brokerage, and restoration services. | ||
Like black back grounds, dislike hookey websites | ||
Cutting-Edge Professional Trendy Sophisticated Modern Elegant Progressive Service Oriented High Tech Masculine |
black backgroung | ||
left side | ||
www.dravelkustom.com | ||
http://www.harborlinebuilds.com/ | ||
http://www.ridgefieldcycleworks.com/ | ||
used logo to coordinate colors | ||

```html
<!DOCTYPE html>
<html lang="en">
<head>
<meta charset="utf-8">
<title>Bluestone Auto Works</title>
<link href="https://fonts.googleapis.com/css2?family=Russo+One&family=Share+Tech&display=swap" rel="stylesheet">
<style>
:root{
  --black:#050505;
  --panel:#1b1b1b;
  --panel-2:#2a2a2a;
  --orange:#f26a0f;
  --orange-dark:#b84a06;
  --hazard:#c9a722;
  --white:#ffffff;
  --text:#e8e8e8;
  --muted:#9a9a9a;
}
*{box-sizing:border-box;margin:0;padding:0}
html,body{width:1200px;height:901px;overflow:hidden;background:var(--black)}
body{position:relative;font-family:"Share Tech",sans-serif;color:var(--text)}
.backdrop{position:absolute;inset:0;background:linear-gradient(135deg,#3a3213 0%,#141108 30%,#0b0b0b 55%,#2e2810 80%,#4a3e14 100%)}
.side-car{position:absolute;bottom:0;width:260px;height:330px}
.side-car.left{left:0;background:radial-gradient(ellipse at 40% 60%,#3b3b3b,#0a0a0a 70%)}
.side-car.right{right:0;background:radial-gradient(ellipse at 60% 60%,#2f6f9a,#0d2233 70%)}
.site{position:absolute;left:170px;top:0;width:852px;height:901px;background:var(--black)}
.masthead{height:49px;display:flex;align-items:stretch;position:relative}
.brand{width:154px;display:flex;align-items:center;gap:8px;padding-left:8px;white-space:nowrap}
.brand-dot{width:16px;height:16px;border-radius:50%;background:var(--orange);flex:none}
.brand-name{font-family:"Russo One",sans-serif;font-size:17px;color:var(--white)}
.nav{flex:1;display:flex;align-items:center;background:var(--orange);font-family:"Russo One",sans-serif;font-size:16px;white-space:nowrap;position:relative}
.nav a{color:var(--black);text-decoration:none;padding:0 7px;height:100%;display:flex;align-items:center;white-space:nowrap}
.nav a.current{background:var(--black);color:var(--white);font-size:22px;padding:0 12px}
.nav .login{margin-left:auto;padding-right:12px;padding-bottom:8px}
.register{position:absolute;right:10px;top:35px;font-size:8px;line-height:10px;color:var(--white);letter-spacing:.3px}
.search{position:absolute;right:8px;top:51px;width:164px;height:16px;background:var(--panel-2);border:1px solid #555;font-size:10px;line-height:14px;color:var(--muted);padding:0 6px}
.search::after{content:"";position:absolute;right:4px;top:2px;width:9px;height:9px;border-radius:50%;border:2px solid #ccc}
.slider{position:absolute;top:68px;left:0;width:852px;height:334px;background:linear-gradient(#3a3a3a,#1e1e1e)}
.slide{position:absolute}
.slide.prev{left:12px;top:26px;width:152px;height:236px;background:linear-gradient(135deg,#6a7eb0,#1a2545)}
.slide.next{right:0;top:26px;width:168px;height:236px;background:linear-gradient(135deg,#2f4aa0,#0b1433)}
.slide.main{left:164px;top:24px;width:474px;height:261px;background:var(--orange);padding:0 43px}
.slide.main .photo{width:100%;height:100%;background:radial-gradient(ellipse at 50% 45%,#c8ccd0,#4c5055 45%,#0e0e0e 80%)}
.arrow{position:absolute;top:140px;width:38px;height:38px;border-radius:50%;background:rgba(255,255,255,.85);display:flex;align-items:center;justify-content:center}
.arrow.left{left:168px}.arrow.right{right:222px}
.dots{position:absolute;top:303px;left:340px;display:flex;align-items:center;gap:8px}
.dots i{width:9px;height:9px;border-radius:50%;background:var(--orange)}
.dots i.on{background:#3a8ed6}
.feature{position:absolute;top:402px;left:0;width:852px;height:474px;background:radial-gradient(ellipse at 70% 30%,#5a1a12 0%,#2a0d0a 35%,#0a0a0a 70%)}
.feature-brand{position:absolute;left:13px;top:22px;display:flex;align-items:center;gap:10px}
.feature-brand .brand-dot{width:36px;height:36px}
.feature-brand .brand-name{font-size:36px}
.tagline{position:absolute;left:0;top:80px;width:280px;height:73px;background:linear-gradient(90deg,var(--orange),var(--orange-dark));font-size:14px;line-height:17px;text-align:center;padding:4px 30px;color:var(--white);clip-path:polygon(0 0,100% 0,92% 100%,0 100%)}
.columns{position:absolute;top:196px;left:13px;right:13px;display:flex;justify-content:space-between}
.col{width:250px}
.col h2{font-family:"Russo One",sans-serif;font-size:26px;color:var(--white);display:flex;align-items:center;gap:8px;margin-bottom:14px;white-space:nowrap}
.col h2::before{content:"";width:26px;height:26px;border-radius:50%;border:3px solid var(--orange);flex:none}
.col p{font-size:15px;line-height:19px;color:var(--white);height:95px}
.more{display:inline-block;margin-top:8px;background:var(--panel-2);border-radius:4px;padding:3px 12px;font-size:13px;color:var(--white)}
.thumbs{position:absolute;left:122px;top:389px;width:720px;height:78px;display:flex;align-items:center;gap:10px}
.thumbs .nav-btn{width:24px;height:24px;border-radius:50%;background:#555}
.thumb{width:105px;height:72px;background:linear-gradient(135deg,#444,#0d0d0d);border:2px solid #333}
.thumb.lit{background:linear-gradient(135deg,#e4e4e4,#6b6b6b)}
.footer{position:absolute;left:0;bottom:0;width:852px;height:25px;background:var(--orange);display:flex;align-items:center;padding:0 12px;font-family:"Russo One",sans-serif;font-size:15px;color:var(--white);white-space:nowrap}
.footer .stay{margin-left:auto;margin-right:14px}
.footer .social{width:18px;height:18px;background:var(--white);margin-left:6px;border-radius:3px}
</style>
</head>
<body>
<div class="backdrop" role="img" aria-label="Dark background with yellow and black hazard tones"></div>
<div class="side-car left" role="img" aria-label="Photo of a black sports car front"></div>
<div class="side-car right" role="img" aria-label="Photo of a blue sports car"></div>

<div class="site">
  <header class="masthead">
    <div class="brand"><span class="brand-dot"></span><span class="brand-name">Bluestone</span></div>
    <nav class="nav">
      <a class="current" href="#">HOME</a><a href="#">SERVICES</a><a href="#">NEWS&amp;EVENTS</a><a href="#">INVENTORY</a><a href="#">CONTACT</a><a href="#">BLOG</a><a class="login" href="#">LOG IN</a>
      <span class="register">REGISTER</span>
    </nav>
  </header>
  <div class="search">Search</div>

  <section class="slider">
    <div class="slide prev" role="img" aria-label="Photo of a classic blue car"></div>
    <div class="slide main"><div class="photo" role="img" aria-label="Photo of a silver muscle car with black stripes"></div></div>
    <div class="slide next" role="img" aria-label="Photo of a blue muscle car"></div>
    <div class="arrow left"><svg width="16" height="16" viewBox="0 0 16 16"><path d="M11 2 4 8l7 6" fill="none" stroke="#f26a0f" stroke-width="3"/></svg></div>
    <div class="arrow right"><svg width="16" height="16" viewBox="0 0 16 16"><path d="M5 2l7 6-7 6" fill="none" stroke="#f26a0f" stroke-width="3"/></svg></div>
    <div class="dots">
      <svg width="14" height="14" viewBox="0 0 14 14"><path d="M10 1 3 7l7 6" fill="none" stroke="#f26a0f" stroke-width="3"/></svg>
      <i class="on"></i><i></i><i></i><i></i><i></i>
      <svg width="14" height="14" viewBox="0 0 14 14"><path d="M4 1l7 6-7 6" fill="none" stroke="#f26a0f" stroke-width="3"/></svg>
    </div>
  </section>

  <section class="feature" role="img" aria-label="Photo of a dark red muscle car in shadow">
    <div class="feature-brand"><span class="brand-dot"></span><span class="brand-name">Bluestone</span></div>
    <div class="tagline">IF YOU ARE LOOKING FOR A HIGH QUALITY CAR THEN YOU HAVE CAME TO RIGHT PLACE</div>
    <div class="columns">
      <article class="col">
        <h2>ABOUT US</h2>
        <p>whatever is your company's description you can describe it here.<br>whatever is your company's description you can describe it here.</p>
        <span class="more">Read more</span>
      </article>
      <article class="col">
        <h2>BUY/SELL</h2>
        <p>Bluestone's services<br>Bluestone's services<br>Bluestone's services<br>Bluestone's services</p>
        <span class="more">Read more</span>
      </article>
      <article class="col">
        <h2>FINANCING</h2>
        <p>your updates regarding this section can be displayed here.<br>Bluestone's updates</p>
        <span class="more">Read more</span>
      </article>
    </div>
    <div class="thumbs">
      <span class="nav-btn"></span>
      <div class="thumb" role="img" aria-label="Thumbnail photo of a black car"></div>
      <div class="thumb lit" role="img" aria-label="Thumbnail photo of a silver car"></div>
      <div class="thumb" role="img" aria-label="Thumbnail photo of a dark car"></div>
      <div class="thumb" role="img" aria-label="Thumbnail photo of a grey car"></div>
      <div class="thumb" role="img" aria-label="Thumbnail photo of a red car"></div>
      <span class="nav-btn"></span>
    </div>
  </section>

  <footer class="footer">
    <span>COPYRIGHT ALL RIGHTS RESERVED</span>
    <span class="stay">STAY UPDATED</span>
    <span class="social"></span><span class="social"></span><span class="social"></span>
  </footer>
</div>
</body>
</html>
```